Virtual Assistant/Online Marketing Business Card/Stationary

I need a professional but modern business card/stationary for my company in Dallas called Brivolo. Brivolo is a virtual assistant specializing in online marketing. I would like a unique design that stands out and makes my brand clear. Incorporating the logo is a must and have attached it to this brief.

Target Market(s)

small business owners & entrepreneurs, 35-65

Industry/Entity Type

Business

Contact Information for Business Card

Maren Tolk
marentolk@brivolo.biz
(555) 271-9064
brivolo.biz

Font styles to use
Sans Serif

Colors
f04a50
3176b5
9bcb3c

Requirements
Must have
• Colors that match the logo colors. Logo integration

```html
<!DOCTYPE html>
<html lang="en">
<head>
<meta charset="utf-8">
<title>Brivolo – Business Card</title>
<link rel="stylesheet" href="https://fonts.googleapis.com/css2?family=Open+Sans:wght@400;600;700&display=swap">
<style>
  :root {
    --page-bg: #e9e7e3;
    --teal: #3aa6b1;
    --charcoal: #2a2a2c;
    --ink: #333335;
    --muted: #5b5b5e;
    --white: #ffffff;
    --blue: #3176b5;
    --green: #9bcb3c;
    --red: #f04a50;
  }
  * { box-sizing: border-box; margin: 0; padding: 0; }
  html, body {
    width: 1200px; height: 950px; overflow: hidden;
    background: var(--page-bg);
    font-family: "Open Sans", Arial, sans-serif;
  }
  .canvas { position: relative; width: 1200px; height: 950px; }

  .card {
    position: absolute;
    width: 700px; height: 400px;
    overflow: hidden;
    box-shadow: 0 10px 24px rgba(0,0,0,0.18);
  }

  /* Back side */
  .card-back {
    left: 100px; top: 60px;
    background: var(--teal);
    color: var(--white);
  }
  .card-back .brand-name {
    position: absolute; left: 0; right: 0; top: 140px;
    text-align: center;
    font-weight: 700; font-size: 64px; letter-spacing: 1px;
  }
  .card-back .web-address {
    position: absolute; left: 0; right: 0; top: 258px;
    text-align: center;
    font-size: 15px; letter-spacing: 5px;
  }

  /* Front side */
  .card-front {
    left: 400px; top: 490px;
    background: var(--white);
  }
  .card-front .header-band { position: absolute; inset: 0; }
  .card-front .holder-name {
    position: absolute; right: 34px; top: 24px;
    color: var(--teal); font-size: 22px; font-weight: 600;
  }
  .card-front .faint-brand {
    position: absolute; right: 30px; top: 170px;
    font-weight: 700; font-size: 96px;
    color: var(--red); opacity: 0.07;
  }
  .card-front .brand-lockup {
    position: absolute; left: 48px; top: 196px;
    display: flex; align-items: center; gap: 12px;
  }
  .brand-dot {
    width: 22px; height: 22px; border-radius: 50%;
    background: var(--red);
  }
  .card-front .brand-name {
    font-weight: 700; font-size: 60px; line-height: 1;
    color: var(--charcoal); letter-spacing: -1px;
  }
  .contact-list {
    position: absolute; left: 52px; top: 304px;
    list-style: none;
  }
  .contact-list li {
    display: flex; align-items: center; gap: 10px;
    font-size: 16px; color: var(--muted); line-height: 26px;
  }
  .contact-list svg { width: 14px; height: 14px; fill: var(--charcoal); }
</style>
</head>
<body>
<main class="canvas">

  <section class="card card-back">
    <div class="brand-name">Brivolo</div>
    <div class="web-address">www.brivolo.biz</div>
  </section>

  <section class="card card-front">
    <svg class="header-band" viewBox="0 0 700 400" width="700" height="400">
      <defs>
        <linearGradient id="accent-stripe" x1="0" y1="0" x2="1" y2="0">
          <stop offset="0" stop-color="#3176b5"/>
          <stop offset="0.12" stop-color="#3176b5"/>
          <stop offset="0.12" stop-color="#9bcb3c"/>
          <stop offset="0.42" stop-color="#9bcb3c"/>
          <stop offset="0.42" stop-color="#f04a50"/>
          <stop offset="0.68" stop-color="#f04a50"/>
          <stop offset="0.68" stop-color="#3aa6b1"/>
          <stop offset="1" stop-color="#3aa6b1"/>
        </linearGradient>
      </defs>
      <path d="M0,0 H700 V88 Q360,80 0,172 Z" fill="#2a2a2c"/>
      <path d="M0,175 Q360,83 700,91" fill="none" stroke="url(#accent-stripe)" stroke-width="7"/>
    </svg>

    <div class="holder-name">Maren Tolk</div>
    <div class="faint-brand" aria-hidden="true">Brivolo</div>

    <div class="brand-lockup">
      <span class="brand-dot"></span>
      <span class="brand-name">Brivolo</span>
    </div>

    <ul class="contact-list">
      <li>
        <svg viewBox="0 0 24 24"><path d="M6.6 10.8a15.1 15.1 0 0 0 6.6 6.6l2.2-2.2a1 1 0 0 1 1-.25 11.4 11.4 0 0 0 3.6.57 1 1 0 0 1 1 1V20a1 1 0 0 1-1 1A17 17 0 0 1 3 4a1 1 0 0 1 1-1h3.5a1 1 0 0 1 1 1 11.4 11.4 0 0 0 .57 3.6 1 1 0 0 1-.25 1z"/></svg>
        (555) 271-9064
      </li>
      <li>
        <svg viewBox="0 0 24 24"><path d="M2 5h20v14H2z M2 5l10 8 10-8" fill="none" stroke="#2a2a2c" stroke-width="2.4"/></svg>
        marentolk@brivolo.biz
      </li>
      <li>
        <svg viewBox="0 0 24 24"><circle cx="12" cy="12" r="10"/><path d="M2 12h20M12 2c3 3 3 17 0 20M12 2c-3 3-3 17 0 20" fill="none" stroke="#ffffff" stroke-width="1.6"/></svg>
        www.brivolo.biz
      </li>
    </ul>
  </section>

</main>
</body>
</html>
```